Design 2 Print Banners for Conference Booth

We need a tall banner and a table banner rough designed for our Conference Booth. The link shows the current booth and what details for banner dimensions and text
see complete design brief here .. https://files.quorvane.net/doc/7TqkXWPLR24ZnaHvB83dKsYtwUEpMRVNC5xa0LdJoq/view?mode=share

Target Market(s)

Doctors & Medical Professionals

Industry/Entity Type

Brimsel

Colors
33a6d7
cee9f5
ecf7fb

Requirements
Must have
• match our branding colors - see current booth backdrop and our website pelvontrix.com

```html
<!DOCTYPE html>
<html lang="en">
<head>
<meta charset="utf-8">
<title>Pelvontrix Labs – Practice Revenue Banner</title>
<link href="https://fonts.googleapis.com/css2?family=Roboto+Condensed:wght@300;400;700&display=swap" rel="stylesheet">
<style>
  :root {
    --brand-blue: #33a6d7;
    --brand-blue-deep: #2a93c9;
    --panel-tint: #ecf7fb;
    --panel-soft: #cee9f5;
    --body-text: #333a3f;
    --page-bg: #ffffff;
    --shadow: rgba(0, 0, 0, 0.35);
    --photo-light: #f2e98a;
    --photo-mid: #a9c93c;
    --photo-deep: #4f8a1f;
  }
  * { box-sizing: border-box; margin: 0; padding: 0; }
  html, body {
    width: 1200px; height: 619px; overflow: hidden;
    background: var(--page-bg);
    font-family: "Roboto Condensed", "Arial Narrow", sans-serif;
  }
  .banner {
    position: absolute; left: 61px; top: 36px;
    width: 1082px; height: 540px;
    background: var(--panel-tint);
    box-shadow: 4px 4px 3px var(--shadow);
    overflow: hidden;
  }
  .headline {
    position: absolute; left: 61px; top: 46px;
    font-size: 29px; line-height: 36px; font-weight: 700;
    color: var(--brand-blue); text-align: center;
  }
  .section-title {
    position: absolute; left: 61px;
    font-size: 19px; font-weight: 300; color: var(--brand-blue);
  }
  .benefits-title { top: 135px; }
  .staff-title { top: 311px; }
  .bullet-list {
    position: absolute; left: 61px; list-style: none;
    font-size: 19.5px; font-weight: 400; color: var(--body-text);
    line-height: 32px;
  }
  .bullet-list li::before { content: "• "; }
  .benefits-list { top: 163px; }
  .staff-list { top: 340px; }
  .cta-note {
    position: absolute; left: 61px; top: 461px;
    font-size: 17px; font-weight: 400; color: var(--brand-blue);
  }
  .url-bar {
    position: absolute; left: 0; top: 490px;
    width: 620px; height: 50px;
    background: var(--brand-blue);
  }
  .url-bar span {
    position: absolute; left: 61px; top: 9px;
    font-size: 26px; font-weight: 400; color: #fff;
  }
  .photo {
    position: absolute; left: 0; top: 0;
    width: 1082px; height: 540px;
  }
  .brand-name {
    position: absolute; left: 770px; top: 62px;
    display: flex; align-items: center; gap: 12px;
    font-size: 40px; font-weight: 400; color: var(--brand-blue-deep);
  }
  .brand-name .brand-dot {
    width: 30px; height: 30px; border-radius: 50%;
    background: var(--brand-blue-deep);
  }
</style>
</head>
<body>
  <main class="banner">
    <h1 class="headline">The Easiest Way To Dramatically Increase<br>Practice Revenue &amp; Serve Patients Better</h1>

    <h2 class="section-title benefits-title">Practice Benefits</h2>
    <ul class="bullet-list benefits-list">
      <li>Nothing to purchase</li>
      <li>No added burden to you or your staff</li>
      <li>No new patients required</li>
      <li>Never any out of pocket expenses</li>
    </ul>

    <h2 class="section-title staff-title">Let Our Highly Trained Staff Handle Everything</h2>
    <ul class="bullet-list staff-list">
      <li>Insurance verification &amp; scheduling</li>
      <li>Most thorough testing &amp; treatment available</li>
      <li>Allergy billing expertise &gt;99%+ collection rate</li>
    </ul>

    <p class="cta-note">Request a complimentary analysis of your revenue potential</p>
    <div class="url-bar"><span>www.pelvontrix.com/allergyincome</span></div>

    <svg class="photo" viewBox="0 0 1082 540" role="img" aria-label="Photo: a relaxed man lying in a sunny meadow of green grass and yellow dandelions">
      <defs>
        <linearGradient id="meadow" x1="0" y1="0" x2="0.3" y2="1">
          <stop offset="0" stop-color="var(--photo-light)"/>
          <stop offset="0.3" stop-color="var(--photo-mid)"/>
          <stop offset="0.75" stop-color="var(--photo-deep)"/>
          <stop offset="1" stop-color="var(--photo-mid)"/>
        </linearGradient>
        <linearGradient id="sky-band" x1="0" y1="0" x2="0" y2="1">
          <stop offset="0" stop-color="#fbf6c8" stop-opacity="0.85"/>
          <stop offset="1" stop-color="#f4ec9a" stop-opacity="0.55"/>
        </linearGradient>
        <clipPath id="arc-clip">
          <path d="M779 0 C 640 110, 560 300, 583 540 L 1082 540 L 1082 0 Z"/>
        </clipPath>
      </defs>
      <g clip-path="url(#arc-clip)">
        <rect x="540" y="0" width="542" height="540" fill="url(#meadow)"/>
        <rect x="540" y="20" width="542" height="128" fill="url(#sky-band)"/>
      </g>
    </svg>

    <div class="brand-name"><span class="brand-dot"></span>Pelvontrix Labs</div>
  </main>
</body>
</html>
```